Flyer needed to promote gutter clearance service for established gardening company

We need a bright and engaging flyer to be designed to advertise our gutter clearance service.
Whilst we are a gardening company that normally does more horticultural work, during the winter we offer other services such as gutter clearance where we remove the debris from gutters and thereby reducing the risk of clogs, leakage, breakage and potential structural damage to the property.

Full details of our service, together with our overall brand and colours can be seen on www.marlowtreecare.co.uk/gutters.

We would like you to use the page on the website as a basis to create the flyer and so please feel free to use as much or as little of the wording contained within the webpage on the flyer drawing particular attention to "Prices starting at just £60 for an average 3 bed house". I will upload pictures but please feel free to use other graphics and fonts to make it stand out.

The contact details which should be included within the flyer are as follows:

Marlow Treecare Services Ltd
Orbit Trading Centre
Fairbrook Vale Ind Estate
Swindon
SN4 7HW

Tel: 01793 418302
www.marlowtreecare.co.uk
dean@marlowtreecare.co.uk

The flyers will eventually be printed out in A5 (210mm x 148mm) using Printelle and so needs to be in that size and suitable file for upload.

I have only put this as a 2 day project as its really urgent and I'm hoping we get some great designs in that time.

Target Market(s)

Homeowners between 25 - 65+

Industry/Entity Type

Home Improvement

Font styles to use
Serif
Sans Serif
Decorative
Script

Colors
6b449b
9bcb3c

Requirements
Must have
• Our colours are purple and green as seen on our website www.marlowtreecare.co.uk/gutters. Please use those colours.
• The flyer should draw attention to the following facts:
• We are Marlow Treecare Services Ltd (see attached logo)
• We are offering a Gutter Clearance Service in Swindon
• Prices start at just £60 for the average 3 bed house.
• We are fully insured.
• Our contact details must be included (as in the product description above)
• I have attached pictures but feel free to add other graphics or use fonts to make the flyer more engaging and interesting.
• Additional wording may be taken from the website at the address shown above. You can use as much or as little wording as you like just as long as the message gets across and the flyer contains our contact information and logo and the details shown above.
Nice to have
• I would like a bright and modern design which isn't too busy or cluttered. It should be something that is quick and easy to read.
Should not have
• I don't want it to look too busy or crowded with small type which people just won't read. Whilst I've said you can take whatever wording you want from our website, I'd suggest you don't take it all or too much. I want the main message (as detailed above in 'must haves') to stand out rather than have it contained deep within lots of small type face.

```html
<!DOCTYPE html>
<html lang="en">
<head>
<meta charset="utf-8">
<title>Marlow Treecare Services – Gutter Clearance Flyer</title>
<link rel="stylesheet" href="https://fonts.googleapis.com/css2?family=Montserrat:wght@700;800;900&family=Open+Sans:wght@400;600;700&display=swap">
<style>
  :root {
    --purple: #6b449b;
    --purple-dark: #4e2f76;
    --green: #9bcb3c;
    --green-dark: #7fae28;
    --ink: #3a3a3a;
    --paper: #ffffff;
  }
  * { margin: 0; padding: 0; box-sizing: border-box; }
  html, body { width: 870px; height: 1200px; overflow: hidden; background: var(--paper); }
  .flyer {
    position: relative; width: 870px; height: 1200px; overflow: hidden;
    background: var(--paper);
    font-family: "Open Sans", Arial, sans-serif; color: var(--ink);
  }
  .hero-photo {
    position: absolute; left: 0; top: 0; width: 870px; height: 380px;
    background: linear-gradient(160deg, #d9dde0 0%, #a9b1a4 35%, #8a6a3e 60%, #d08a2a 80%, #6e7a52 100%);
  }
  .brand {
    position: absolute; right: 0; top: 36px; width: 270px; height: 100px;
    background: var(--paper); display: flex; align-items: center; gap: 12px;
    padding-left: 22px;
  }
  .brand-dot { width: 24px; height: 24px; border-radius: 50%; background: var(--green); flex: none; }
  .brand-name {
    font-family: "Montserrat", Arial, sans-serif; font-weight: 800;
    font-size: 24px; line-height: 1.05; color: var(--purple);
  }
  .price-band { position: absolute; left: 0; top: 290px; width: 870px; height: 190px; }
  .price-headline {
    position: absolute; left: 0; top: 366px; width: 870px; text-align: center;
    font-family: "Montserrat", Arial, sans-serif; font-weight: 900;
    font-size: 38px; line-height: 1.15; color: var(--paper); text-transform: uppercase;
  }
  .price-headline .accent { color: var(--green); }
  .col { position: absolute; top: 496px; }
  .col-why { left: 30px; width: 395px; }
  .col-help { left: 448px; width: 392px; }
  .col-heading {
    font-family: "Montserrat", Arial, sans-serif; font-weight: 900;
    font-size: 30px; line-height: 1.05; text-transform: uppercase;
    padding: 10px 18px; height: 76px;
  }
  .col-why .col-heading { background: var(--green); color: var(--purple); }
  .col-help .col-heading { background: var(--purple); color: var(--paper); }
  .col-why .col-body { padding: 12px 6px 0 6px; }
  .col-body p, .help-box p { font-size: 15px; line-height: 1.36; margin-bottom: 10px; }
  .col-why .col-body p { color: var(--purple-dark); }
  .col-why .highlight { color: var(--green-dark); font-weight: 700; }
  .col-why .col-body p.address { color: var(--green-dark); font-weight: 600; text-align: center; margin-top: 4px; }
  .help-box { background: var(--green); padding: 14px 18px 6px; }
  .help-box p { color: var(--paper); }
  .contact-heading {
    margin-top: 12px; background: var(--purple); color: var(--paper);
    font-family: "Montserrat", Arial, sans-serif; font-weight: 900;
    font-size: 32px; padding: 6px 18px; text-transform: uppercase;
  }
  .contact-lines { padding: 8px 18px 0; font-family: "Montserrat", Arial, sans-serif; font-weight: 700; font-size: 19px; line-height: 1.3; color: var(--purple-dark); }
  .contact-lines .tel { color: var(--green-dark); }
  .results { position: absolute; left: 0; top: 1024px; width: 870px; height: 176px; display: flex; }
  .result { position: relative; flex: 1; }
  .result-before { background: linear-gradient(135deg, #6b5a3a, #a07c3e 50%, #4f4a36); }
  .result-after { background: linear-gradient(135deg, #cfd3d6, #e9ecee 50%, #9aa3a8); }
  .result-label {
    position: absolute; bottom: 16px; font-family: "Montserrat", Arial, sans-serif;
    font-weight: 900; font-size: 26px; color: var(--paper); text-transform: uppercase; letter-spacing: 1px;
  }
  .result-before .result-label { left: 110px; }
  .result-after .result-label { left: 20px; }
  .results-divider { position: absolute; left: 433px; top: 0; width: 4px; height: 176px; background: var(--paper); }
  .corner { position: absolute; left: 0; bottom: 0; width: 90px; height: 176px; }
</style>
</head>
<body>
<main class="flyer">
  <div class="hero-photo" role="img" aria-label="Photo of a gloved hand clearing autumn leaves from a house gutter"></div>

  <div class="brand">
    <span class="brand-dot"></span>
    <span class="brand-name">Marlow Treecare Services</span>
  </div>

  <svg class="price-band" viewBox="0 0 870 190" preserveAspectRatio="none" aria-hidden="true">
    <polygon points="0,46 870,0 870,14 0,60" fill="var(--green)"/>
    <polygon points="0,60 870,14 870,190 0,190" fill="var(--purple)"/>
  </svg>
  <h1 class="price-headline">Prices starting at <span class="accent">just £60</span><br>for an average 3 bed house</h1>

  <section class="col col-why">
    <h2 class="col-heading">Why clean<br>gutters?</h2>
    <div class="col-body">
      <p>They play a key role in maintaining the <span class="highlight">structural integrity</span> of your property. Keeping them clean and clear from debris is a great way to avoid damage to your home and potentially expensive gutter repairs</p>
      <p>Accumulation of moss, leaves can result in damp within your home, causing <span class="highlight">potential health issues</span> to you and your family.</p>
      <p>They need to be cleaned at least once per year in order to keep them <span class="highlight">performing properly</span> and to avoid the potential for gutter repairs in the future.</p>
      <p class="address">Marlow Treecare Services Ltd<br>Orbit Trading Centre,<br>Fairbrook Vale Ind Estate, Swindon<br>SN4 7HW</p>
    </div>
  </section>

  <section class="col col-help">
    <h2 class="col-heading">How can we<br>help?</h2>
    <div class="help-box">
      <p>Clearing gutters is not just a dirty job but it can be a dangerous one too if not done properly. At Marlow Treecare Services, we use the latest tools and techniques to safely clear your gutters, giving you peace of mind without having to risk getting dirty or injured yourself.</p>
      <p>And with costs starting at just £60 to clear the gutters of an average 3 bed house, it is an affordable way to get your home prepared for the winter.</p>
    </div>
    <h2 class="contact-heading">Contact us!</h2>
    <div class="contact-lines">
      <div class="tel">Tel: 01793 418302</div>
      <div>www.marlowtreecare.co.uk</div>
      <div>dean@marlowtreecare.co.uk</div>
    </div>
  </section>

  <div class="results">
    <div class="result result-before" role="img" aria-label="Photo of a gutter clogged with leaves before clearing">
      <span class="result-label">Before</span>
    </div>
    <div class="result result-after" role="img" aria-label="Photo of a clean gutter after clearing">
      <span class="result-label">After</span>
    </div>
    <div class="results-divider"></div>
  </div>
  <svg class="corner" viewBox="0 0 90 176" aria-hidden="true">
    <polygon points="0,0 90,176 0,176" fill="var(--green)"/>
  </svg>
</main>
</body>
</html>
```